MEDICAL CLINIC LETTERHEAD

Design is a letterhead for a non-profit medical center. The name of the clinic is VYRLOTEN Community Health Center. Although the full name must be included, the community health center part is more of a description and should be less visible - i attached an example of what I mean by that (ATTACHED IMAGE IS AN EXAMPLE OF FONT SIZES NOT A DESIGN IDEA). Please design something modern, cool looking and unique because I can always download free templates.
Phone, email, website and etc will be added later.

Industry/Entity Type

MEDICAL

```html
<!DOCTYPE html>
<html lang="en">
<head>
<meta charset="utf-8">
<title>VYRLOTEN Community Health Center Letterhead</title>
<link rel="stylesheet" href="https://fonts.googleapis.com/css2?family=Montserrat:wght@700&family=Questrial&family=Roboto:wght@400&display=swap">
<style>
  :root {
    --navy: #0d2a54;
    --grey-bar: #9a9a9a;
    --paper: #fbfbfb;
    --ink: #575757;
    --ink-soft: #6a6a6a;
    --rule: #c9c9c9;
  }
  * { box-sizing: border-box; margin: 0; padding: 0; }
  html, body { width: 1023px; height: 1200px; overflow: hidden; background: var(--paper); }
  .letterhead { position: relative; width: 1023px; height: 1200px; background: var(--paper); overflow: hidden; }

  .brand { position: absolute; left: 97px; top: 96px; }
  .brand-name {
    font-family: "Montserrat", sans-serif; font-weight: 700;
    font-size: 45px; line-height: 1; color: var(--navy); letter-spacing: 0.5px;
  }
  .brand-tagline {
    font-family: "Questrial", sans-serif; font-size: 14px; color: var(--ink-soft);
    letter-spacing: 3.4px; margin-top: 5px; padding-left: 1px;
  }

  .contact {
    position: absolute; left: 736px; top: 76px; height: 96px;
    border-left: 1px solid var(--rule); padding-left: 23px;
    font-family: "Roboto", sans-serif; font-size: 14px; color: var(--ink); line-height: 17px;
  }
  .contact-address { margin: 0 0 5px; }
  .contact-line { display: flex; align-items: center; gap: 7px; }
  .contact-line svg { width: 12px; height: 12px; flex: none; }

  .letter {
    position: absolute; left: 97px; top: 318px; width: 841px;
    font-family: "Questrial", sans-serif; color: var(--ink);
  }
  .salutation { font-size: 17px; margin-bottom: 32px; }
  .letter p.body {
    font-size: 14px; line-height: 18.3px; text-align: justify; margin-bottom: 18px;
  }
  .letter p.body.spaced { margin-bottom: 36px; }
  .closing { font-size: 14px; margin-top: 72px; }

  .footer-band { position: absolute; left: 0; bottom: 0; height: 12px; }
  .footer-band.primary { width: 652px; background: var(--navy); }
  .footer-band.secondary { left: 655px; right: 0; background: var(--grey-bar); }
</style>
</head>
<body>
<main class="letterhead">
  <header class="brand">
    <div class="brand-name">VYRLOTEN</div>
    <div class="brand-tagline">COMMUNITY HEALTH CENTER</div>
  </header>

  <address class="contact" style="font-style: normal;">
    <p class="contact-address">PO Box 412 Marrowfield<br>Lakeland 60214</p>
    <div class="contact-line">
      <svg viewBox="0 0 24 24" aria-hidden="true"><path fill="var(--navy)" d="M6.6 10.8a15.1 15.1 0 0 0 6.6 6.6l2.2-2.2c.3-.3.7-.4 1-.2 1.1.4 2.3.6 3.6.6.6 0 1 .4 1 1V20c0 .6-.4 1-1 1C10.6 21 3 13.4 3 4c0-.6.4-1 1-1h3.5c.6 0 1 .4 1 1 0 1.3.2 2.5.6 3.6.1.3 0 .7-.2 1z"/></svg>
      <span>(555) 310.4827</span>
    </div>
    <div class="contact-line">
      <svg viewBox="0 0 24 24" aria-hidden="true"><rect x="2" y="5" width="20" height="14" rx="1.5" fill="var(--navy)"/><path d="M3 6.5l9 6.5 9-6.5" fill="none" stroke="var(--paper)" stroke-width="1.8"/></svg>
      <span>info@vyrloten.org</span>
    </div>
    <div class="contact-line">
      <svg viewBox="0 0 24 24" aria-hidden="true"><circle cx="12" cy="12" r="10" fill="var(--navy)"/><path d="M2 12h20M12 2c3 3 3 17 0 20M12 2c-3 3-3 17 0 20" fill="none" stroke="var(--paper)" stroke-width="1.3"/></svg>
      <span>www.vyrloten.org</span>
    </div>
  </address>

  <section class="letter">
    <p class="salutation">Dear Alex,</p>
    <p class="body">Donec malesuada orci vitae nulla accumsan porta a id massa. Quisque accumsan iaculis magna sit amet fringilla. Maecenas consequat, magna eget tincidunt semper, odio nibh rutrum mi, id feugiat ante nisi eu risus. Vestibulum nunc orci, rhoncus a placerat in, ultricies in mi. Cras mattis varius eros, vel fringilla nisi suscipit eget. Quisque scelerisque sagittis nulla at porttitor.</p>
    <p class="body spaced">Lorem ipsum dolor sit amet, consectetur adipiscing elit. Donec orci purus, luctus vitae dignissim eu, iaculis sed purus. Vivamus faucibus, ipsum nec aliquet viverra, leo mauris condimentum ligula, sit amet sagittis enim ligula quis arcu. Nam egestas tortor id nisi porttitor mattis. In tortor ante, ultricies in suscipit a, tempus non massa. Vivamus et auctor mi. Fusce vel massa nulla. Phasellus nec eros mauris, et scelerisque orci.</p>
    <p class="body">It is a long established fact that a reader will be distracted by the readable content of a page when looking at its layout. The point of using Lorem Ipsum is that it has a more-or-less normal distribution of letters, as opposed to using 'Content here, content here', making it look like readable English. Many desktop publishing packages</p>
    <p class="body">Sed id augue vitae urna euismod commodo aliquet a quam. Pellentesque arcu velit, cursus et malesuada ut, consequat et diam. Nullam erat sem, rhoncus id ullamcorper vitae, rhoncus et arcu. In ultricies ultricies nulla, ut rutrum nisi iaculis at. Donec eu magna a metus ornare faucibus. Fusce aliquet faucibus ultricies. Morbi semper, est id tincidunt gravida, sem arcu adipiscing lacus, ac bibendum nulla leo eu purus. Quisque nec diam sed risus consectetur a ccumsan quis quis nibh. Vestibulum id purus lorem.</p>
    <p class="closing">Sincerely,</p>
  </section>

  <div class="footer-band primary"></div>
  <div class="footer-band secondary"></div>
</main>
</body>
</html>
```